'Cradle Ahead' promotional brochure

We have designed a 6 week program to educate impending first-time parents about the things they need to know to survive the first 6 months. Sessions delivered by general practitioner/family doctor, dietician, physiotherapist, speech pathologist and psychologist. Our promotional blurb is: 'A comprehensive education program for first-time parents-to-be, delivered over 6 weeks by health professionals in your community, about everything you need to know to look after your baby (and yourself!) in the first 6 months'. I now want to put together a promotional brochure to be distributed to those couples who express an interest which will provide further details of what will be delivered in the course.
Updates
In terms of layout, I envisaged a double sided A4 size, foldable into 3 sections, but very happy to be guided on this.
Target Market(s)
To appeal to a young, well educated demographic. First time parents couples.
Industry/Entity Type
Medical
Font styles to use
Other font styles liked:
- Playfair Display
Requirements
Must have
- Playfair display font to be consistent with our logo (attached). Logo also included please. Some consistency with colours of logo please.
Nice to have
- I am a doctor, and have no creative genes! But prefer a clean and professional appearance overall. Not too cluttered in overall appearance.
Should not have
- No cheesy pictures of babies.

```html
<!DOCTYPE html>
<html lang="en">
<head>
<meta charset="utf-8">
<title>Cradle Ahead – Program Brochure</title>
<link href="https://fonts.googleapis.com/css2?family=Playfair+Display:wght@700&family=Open+Sans:ital,wght@0,400;0,600;0,700;0,800;1,400;1,700&family=Oswald:wght@300&display=swap" rel="stylesheet">
<style>
  :root{
    --green:#3ea31a;
    --green-deep:#2a7a0c;
    --green-light:#6cc93c;
    --green-bright:#7ee04a;
    --black:#141414;
    --white:#ffffff;
    --paper:#f1f2f0;
    --grey-text:#555a52;
    --red:#d8121b;
    --backdrop:#e8eaec;
  }
  *{box-sizing:border-box;margin:0;padding:0}
  html,body{width:968px;height:1200px;overflow:hidden}
  body{background:var(--backdrop);position:relative;font-family:"Open Sans",Arial,sans-serif;color:var(--white)}
  .sheet{position:absolute;left:79px;width:810px;height:573px;overflow:hidden;box-shadow:0 6px 18px rgba(0,0,0,.18)}
  .sheet--outside{top:18px}
  .sheet--inside{top:609px}
  .sheet__art{position:absolute;inset:0;width:810px;height:573px}
  .block{position:absolute}

  /* outside – back panel */
  .price-badge{left:30px;top:28px;width:104px;height:104px;border-radius:50%;background:var(--red);border:7px solid #e9efe4;display:flex;flex-direction:column;align-items:center;justify-content:center;font-weight:800;font-style:italic;line-height:1}
  .price-badge__label{font-size:12px;letter-spacing:.5px}
  .price-badge__amount{font-size:30px}
  .benefits{left:22px;top:152px;width:232px;list-style:none;font-size:9px;font-style:italic;line-height:1.3}
  .benefits li{position:relative;padding-left:13px;margin-bottom:8px}
  .benefits li::before{content:"";position:absolute;left:0;top:3px;width:6px;height:6px;border:1.5px solid var(--white);border-radius:50%}
  .notice{left:20px;top:440px;width:230px;font-size:9px;color:var(--black);line-height:1.3}

  /* outside – middle panel */
  .hours{left:280px;top:30px;width:250px;text-align:center;font-size:9.5px;line-height:1.35}
  .hours__title{font-weight:800;font-size:13px;margin-bottom:4px;letter-spacing:.3px}
  .map{left:350px;top:168px;width:110px;height:110px;border-radius:50%;border:6px solid #dfe9d8;background:radial-gradient(circle at 70% 60%,#9cc8e8 0 30%,#e7ead8 31%)}
  .contact{left:280px;top:336px;width:250px;color:var(--black);font-size:9px;line-height:1.55}
  .contact__title{color:var(--green);font-weight:800;font-size:12.5px;text-align:center;line-height:1.2;margin-bottom:8px}
  .contact__row{display:flex;align-items:center;gap:5px}
  .contact__row svg{flex:none;width:9px;height:9px}
  .contact__row--indent{padding-left:14px}

  /* outside – cover */
  .brand-name{left:590px;top:36px;width:200px;display:flex;align-items:center;gap:8px;font-weight:700;font-size:11px;color:var(--white);letter-spacing:.3px}
  .brand-name__mark{flex:none;width:12px;height:12px;background:var(--white)}
  .cover-title{left:582px;top:96px;width:220px;font-family:"Playfair Display",Georgia,serif;font-weight:700;color:var(--white);font-size:44px;line-height:1.02}

  /* inside */
  .week-tag{display:inline-block;background:var(--white);color:var(--green);font-weight:800;font-style:italic;font-size:10.5px;padding:2px 18px 2px 8px;clip-path:polygon(0 0,86% 0,100% 50%,86% 100%,0 100%);margin-bottom:4px}
  .session{font-size:7.4px;line-height:1.35}
  .session strong{font-weight:700}
  .topics{list-style:none;font-size:7.2px;line-height:1.3;margin-top:2px}
  .topics li{position:relative;padding-left:9px}
  .topics li::before{content:"";position:absolute;left:0;top:2.5px;width:4px;height:4px;border:1px solid var(--white);border-radius:50%}
  .week--1{left:16px;top:14px;width:240px}
  .week--2{left:16px;top:138px;width:240px}
  .week--3{left:298px;top:150px;width:236px;color:var(--grey-text)}
  .week--3 .week-tag{background:var(--green);color:var(--white)}
  .middle-intro{left:298px;top:70px;width:236px;color:var(--grey-text)}
  .week--4{left:562px;top:190px;width:234px}
  .week--5{left:562px;top:322px;width:234px}
  .week--6{left:562px;top:418px;width:234px}
  .family-photo{left:60px;top:250px;width:150px;height:150px;border-radius:50%;background:radial-gradient(circle at 45% 40%,#f3e4d6,#cdb39c 60%,#8f8a86);border:4px solid var(--white)}
  .brand-disc{left:40px;top:350px;width:132px;height:132px;border-radius:50%;background:var(--green-light);display:flex;align-items:center;justify-content:center;text-align:center;font-size:15px;line-height:1.2;padding:14px}
  .tagline{left:190px;top:366px;width:340px;font-family:"Oswald","Arial Narrow",sans-serif;font-weight:300;color:var(--green-bright);font-size:27px;line-height:1.05}
  .about{left:190px;top:480px;width:330px;font-size:8px;line-height:1.4}
  .clinic-photo{left:545px;top:0;width:265px;height:180px;background:linear-gradient(160deg,#d7f27a,#9ed12f 55%,#5f9a16);border-bottom-left-radius:60% 45%}
</style>
</head>
<body>

<section class="sheet sheet--outside" aria-label="Brochure outside">
  <svg class="sheet__art" viewBox="0 0 810 573" aria-hidden="true">
    <defs>
      <linearGradient id="outGreen" x1="0" y1="0" x2="1" y2="1">
        <stop offset="0" stop-color="#47b21e"/><stop offset="1" stop-color="#2c820f"/>
      </linearGradient>
      <clipPath id="coverClip"><rect x="540" y="0" width="270" height="573"/></clipPath>
    </defs>
    <rect width="810" height="573" fill="url(#outGreen)"/>
    <path d="M0,120 C200,60 420,160 810,40 L810,0 L0,0 Z" fill="#ffffff" opacity=".06"/>
    <path d="M0,250 C180,180 380,300 540,220" stroke="#ffffff" stroke-opacity=".12" stroke-width="30" fill="none"/>
    <path d="M0,360 C90,300 200,270 300,290 C380,305 460,300 540,270 L540,573 L0,573 Z" fill="#141414"/>
    <path d="M0,392 C110,330 220,310 320,320 C400,328 470,320 540,300 L540,573 L0,573 Z" fill="#f4f5f3"/>
    <path d="M420,573 C470,520 510,470 540,420 L540,573 Z" fill="#141414"/>
    <g clip-path="url(#coverClip)">
      <circle cx="760" cy="470" r="230" fill="#5cc02c"/>
      <circle cx="770" cy="480" r="215" fill="#141414"/>
    </g>
    <line x1="270" y1="0" x2="270" y2="573" stroke="#000" stroke-opacity=".08"/>
    <line x1="540" y1="0" x2="540" y2="573" stroke="#000" stroke-opacity=".08"/>
  </svg>
  <div class="block" role="img" aria-label="Photo of a newborn's feet held in a parent's hands"
       style="left:560px;top:262px;width:250px;height:311px;border-top-left-radius:100% 80%;background:radial-gradient(circle at 60% 40%,#f4d4c6,#d9a48f 55%,#a9786a)"></div>

  <div class="block price-badge"><span class="price-badge__label">TOTAL COST</span><span class="price-badge__amount">$300</span></div>
  <ul class="block benefits">
    <li>A Comprehensive Education Program for First Time Parents.</li>
    <li>Delivered Over 6 Weeks by Health Professionals in Your Community</li>
    <li>Everything You Need to Know to Look After Your baby (And Yourself!) IN THE FIRST 6 MONTHS.</li>
  </ul>
  <p class="block notice">Please note this email service is checked once daily and is not available for making appointments or accessing medical advice.</p>

  <div class="block hours">
    <p class="hours__title">OPENING HOURS</p>
    <p>Monday to Friday: 8:30am – 5:00pm</p>
    <p>Saturday: 8:00am – 12:00pm</p>
    <p>Sunday &amp; Public Holidays: Closed</p>
  </div>
  <div class="block map" role="img" aria-label="Street map showing the clinic location"></div>
  <div class="block contact">
    <p class="contact__title">CONTACT DETAILS<br>FOR ENQUIRIES BOOKINGS</p>
    <p class="contact__row contact__row--indent"><svg viewBox="0 0 10 10"><path d="M2,1 L4,1 L4.5,3 L3.5,4 C4,5.5 5,6.5 6,6.5 L7,5.5 L9,6 L9,8 C5,9 1,5 2,1 Z" fill="#141414"/></svg>02 5550 0188</p>
    <p class="contact__row contact__row--indent"><svg viewBox="0 0 10 10"><rect x="1" y="3" width="8" height="6" fill="#141414"/><rect x="3" y="1" width="4" height="3" fill="#141414"/></svg>02 5550 0199</p>
    <p class="contact__row"><svg viewBox="0 0 10 10"><path d="M5,0.5 C2.5,0.5 1.5,2.5 1.5,4 C1.5,6.5 5,9.5 5,9.5 C5,9.5 8.5,6.5 8.5,4 C8.5,2.5 7.5,0.5 5,0.5 Z" fill="#141414"/><circle cx="5" cy="4" r="1.3" fill="#fff"/></svg>Wattlebrook Shopping Village, Shop 11</p>
    <p class="contact__row contact__row--indent">48 Wattlebrook Way Wattlebrook NSW 2400</p>
    <p class="contact__row"><svg viewBox="0 0 10 10"><rect x="0.5" y="2" width="9" height="6" fill="#141414"/><path d="M0.5,2 L5,5.5 L9.5,2" stroke="#fff" stroke-width="0.8" fill="none"/></svg>reception@wattlebrookhealth.com.au</p>
    <p class="contact__row"><svg viewBox="0 0 10 10"><rect x="0.5" y="3" width="5" height="3" rx="1.5" stroke="#141414" stroke-width="1.2" fill="none"/><rect x="4.5" y="4" width="5" height="3" rx="1.5" stroke="#141414" stroke-width="1.2" fill="none"/></svg>www.wattlebrookhealth.com.au</p>
  </div>

  <div class="block brand-name"><span class="brand-name__mark"></span><span>Wattlebrook Health &amp; Medical</span></div>
  <h1 class="block cover-title">Cradle<br>Ahead</h1>
</section>

<section class="sheet sheet--inside" aria-label="Brochure inside">
  <svg class="sheet__art" viewBox="0 0 810 573" aria-hidden="true">
    <defs>
      <linearGradient id="inGreen" x1="0" y1="0" x2="1" y2="1">
        <stop offset="0" stop-color="#4ab61f"/><stop offset="1" stop-color="#2e860f"/>
      </linearGradient>
    </defs>
    <rect width="810" height="573" fill="url(#inGreen)"/>
    <path d="M0,200 C150,120 300,180 540,90" stroke="#ffffff" stroke-opacity=".1" stroke-width="40" fill="none"/>
    <path d="M285,60 C380,40 470,45 548,70 L548,470 C460,445 370,455 285,500 Z" fill="#f1f2f0"/>
    <path d="M0,460 C70,380 190,350 320,370 C420,385 500,430 548,480 L548,573 L0,573 Z" fill="#141414"/>
    <line x1="270" y1="0" x2="270" y2="573" stroke="#000" stroke-opacity=".06"/>
    <line x1="540" y1="0" x2="540" y2="573" stroke="#000" stroke-opacity=".08"/>
  </svg>

  <div class="block week--1">
    <span class="week-tag">WEEK 1</span>
    <p class="session"><strong>GP Dr Maren Holt will share information for Mum's own health after delivery. Topics include:</strong></p>
    <ul class="topics">
      <li>Complications in pregnancy</li>
      <li>Bleeding, bowel and bladder after delivery</li>
      <li>Breastfeeding, engorgement and mastitis</li>
      <li>Bottle feeding</li>
      <li>Postnatal anxiety &amp; depression</li>
      <li>Intimacy and contraception</li>
    </ul>
  </div>
  <div class="block week--2">
    <span class="week-tag">WEEK 2</span>
    <p class="session"><strong>Session 1 – Clinical Psychologist Dr Anika Ward will discuss changes in relationships as couples become parents, gender roles in parenting and post-natal depression.</strong></p>
  </div>
  <div class="block family-photo" role="img" aria-label="Photo of a smiling family with a young child at a doctor's visit"></div>
  <div class="block brand-disc">Wattlebrook Health &amp; Medical</div>
  <p class="block tagline">Caring for your<br>Health, Listening<br>to your needs</p>
  <p class="block about">As medical practitioners, by getting to know you and your family, we can help not only to treat your illnesses, but also understand the effects of your illness and on those around you.</p>

  <p class="block session middle-intro">Session 2 – Physiotherapist Tessa Moore will present advice for Mums regarding exercise during and after pregnancy, looking after the pelvic floor during and after pregnancy, and abdominal muscle separation management. She will also provide advice on promoting babies' neck strength and minimising the risk of flat spots on the head and encouraging gross motor skills in the first 6 months.</p>
  <div class="block week--3">
    <span class="week-tag">WEEK 3</span>
    <p class="session">Session 1 – Dietician Clare Benton provides advice for Mums regarding healthy eating during pregnancy and lactation, normal weight gain during pregnancy and realistic weight loss after. She will also discuss the evidence regarding breastfeeding vs bottle-feeding, normal infant weight gain and introducing solids (including those with potential for allergy).</p>
    <p class="session" style="margin-top:6px">Session 2 – Paediatric Speech Pathologist Ruth Ellison will share information about latching and breast-feeding troubles &amp; tongue tie, advice about dummies and finger-sucking, introducing solids &amp; feeding (including 'pouch' food), encouraging language development and current evidence about electronic devices impacting language development.</p>
  </div>

  <div class="block clinic-photo" role="img" aria-label="Photo of the bright clinic waiting room"></div>
  <div class="block week--4">
    <span class="week-tag">WEEK 4</span>
    <p class="session"><strong>GP Dr Maren Holt will share advice about your babies' health in the first 6 months, including:</strong></p>
    <ul class="topics">
      <li>Skin of newborns</li>
      <li>Sleeping</li>
      <li>Crying</li>
      <li>Immunisations</li>
      <li>Fever and infections</li>
      <li>Diarrhoea and constipation</li>
      <li>Teething</li>
      <li>Understanding a baby's signals</li>
    </ul>
  </div>
  <div class="block week--5">
    <span class="week-tag">WEEK 5</span>
    <p class="session">Session 1 – Clinical Psychologist Dr Anika Ward will share information about bonding &amp; attachment with your baby, how to promote their social &amp; emotional development and how to manage separation anxiety. She will also discuss positive parenting approaches.</p>
  </div>
  <div class="block week--6">
    <span class="week-tag">WEEK 6</span>
    <p class="session">Session 1 – Secret Men's Business – a men-only session (including beer!) with a new father for frank discussion about the road ahead. Mums will do a shopping excursion with the GP &amp; Dietician to FreshMart to look at baby products and food – the good and the bad!</p>
    <p class="session" style="margin-top:6px">Session 2 – Program review, reflection and evaluation and future session planning when baby is 6 months of age.</p>
  </div>
</section>

</body>
</html>
```